Corvella Paintless Dent Removal

Our company works on vehicles removing dents using a highly skilled trade which the metal is massaged out with special tools without disturbing the original paint, hence paintless dent removal. Besides keeping the paint and metal original its also very environmentally friendly since no paint or toxic fillers are used. Also we we are one of the most experienced companies in the business with 25 years

Target Market(s)

Retail Automobile consumers, Auto Dealerships and Auto Body Shops

Industry/Entity Type

Auto Repair

Contact Information for Business Card

Dennis Holbrook
PO Box 538 Ashmere, NY 11952
631-472-8816
corvellapdr@mailnest.example
website corvellapdr.example
youtube corvella paintless dent removal
25 years of experience removing Dents, Dings and Hail Damage

Font styles to use
Serif
Sans Serif

Colors

Designer to choose colors to be used in the design.

Requirements
Must have
• I do like things that are simple but classy and somewhat bold, also I like my logo so that should be somewhat important

```html
<!DOCTYPE html>
<html lang="en">
<head>
<meta charset="utf-8">
<title>Corvella Paintless Dent Removal — Business Card</title>
<link rel="stylesheet" href="https://fonts.googleapis.com/css2?family=Archivo+Black&family=Open+Sans:wght@400;600&display=swap">
<style>
  :root {
    --backdrop: #505254;
    --card: #1d1e20;
    --card-edge: #2a2b2e;
    --gloss: #3a3c40;
    --brand-blue: #1f5fb8;
    --accent-green: #8cd21e;
    --ink-light: #d9dbde;
  }
  * { box-sizing: border-box; margin: 0; padding: 0; }
  html, body { width: 800px; height: 1200px; overflow: hidden; }
  body {
    background: var(--backdrop);
    font-family: "Open Sans", Arial, sans-serif;
    position: relative;
  }
  .card {
    position: absolute;
    left: 70px;
    width: 660px;
    height: 378px;
    background: var(--card);
    border: 1px solid var(--card-edge);
    border-radius: 4px;
    box-shadow: 0 18px 40px rgba(0,0,0,0.35);
    overflow: hidden;
  }
  .card--front { top: 150px; }
  .card--back { top: 670px; }

  .front-name {
    position: absolute;
    inset: 0;
    display: flex;
    align-items: center;
    justify-content: center;
    font-family: "Archivo Black", Arial, sans-serif;
    font-size: 64px;
    letter-spacing: 1px;
    color: var(--gloss);
    text-transform: uppercase;
  }

  .back-brand {
    position: absolute;
    left: 36px;
    top: 34px;
    font-family: "Archivo Black", Arial, sans-serif;
    color: var(--brand-blue);
    text-transform: uppercase;
    line-height: 1;
  }
  .back-brand .brand-main { display: block; font-size: 44px; }
  .back-brand .brand-sub { display: block; font-size: 17px; margin-top: 4px; letter-spacing: 0.3px; }

  .brand-mark-area {
    position: absolute;
    left: 400px;
    top: 140px;
    width: 190px;
    height: 190px;
    background: var(--brand-blue);
  }

  .contact-person {
    position: absolute;
    left: 36px;
    top: 150px;
    width: 340px;
  }
  .person-name {
    font-size: 24px;
    font-weight: 600;
    color: var(--accent-green);
  }
  .person-title {
    font-size: 12px;
    color: var(--ink-light);
    margin-top: 2px;
  }
  .contact-list {
    list-style: none;
    margin-top: 16px;
  }
  .contact-list li {
    display: flex;
    align-items: center;
    gap: 10px;
    font-size: 13px;
    color: var(--ink-light);
    line-height: 1.25;
    margin-bottom: 7px;
  }
  .contact-list svg { width: 12px; height: 12px; flex: none; fill: var(--accent-green); }
</style>
</head>
<body>
  <section class="card card--front" aria-label="Business card front">
    <div class="front-name">Corvella</div>
  </section>

  <section class="card card--back" aria-label="Business card back">
    <div class="back-brand">
      <span class="brand-main">Corvella</span>
      <span class="brand-sub">Paintless Dent Removal</span>
    </div>

    <div class="brand-mark-area" role="img" aria-label="Large blue brand mark area"></div>

    <div class="contact-person">
      <p class="person-name">Dennis Holbrook</p>
      <p class="person-title">Managing Director</p>
      <ul class="contact-list">
        <li>
          <svg viewBox="0 0 12 12" aria-hidden="true"><path d="M6 0C3.8 0 2 1.8 2 4c0 3 4 8 4 8s4-5 4-8c0-2.2-1.8-4-4-4zm0 5.5A1.5 1.5 0 1 1 6 2.5a1.5 1.5 0 0 1 0 3z"/></svg>
          <span>PO Box 538 Ashmere,<br>NY 11952</span>
        </li>
        <li>
          <svg viewBox="0 0 12 12" aria-hidden="true"><path d="M2.5 0.5l2 2-1 1.5c.7 1.6 2 2.9 3.5 3.5l1.5-1 2 2-1.5 2C4.5 10 2 7.5.5 2z"/></svg>
          <span>631-472-8816</span>
        </li>
        <li>
          <svg viewBox="0 0 12 12" aria-hidden="true"><path d="M0 2h12v1L6 7 0 3zM0 4.5l6 4 6-4V10H0z"/></svg>
          <span>corvellapdr@mailnest.example</span>
        </li>
        <li>
          <svg viewBox="0 0 12 12" aria-hidden="true"><circle cx="6" cy="6" r="5.5"/></svg>
          <span>www.corvellapdr.example</span>
        </li>
      </ul>
    </div>
  </section>
</body>
</html>
```